Design home page for brightvane.xyz

We’re seeking a sleek, lead-generation-focused single-page website for Brightvane.xyz that communicates our expertise in delivering high-intent leads to mid-sized businesses. The goal is to guide visitors toward scheduling a free consultation while emphasizing our performance-based approach and comprehensive service offerings.

Industry/Entity Type

Marketing

Number of Pages Required

1 page

Font styles to use
Sans Serif

Requirements
Must have
• content from https://files.quorvalet.example/doc/7hTmwQRZa93KpLdVyxNe42UcBsFoGj8rYiMn5EkPtWz/view?tab=t.0
Nice to have
• color pallet from here https://files.quorvalet.example/doc/4pRkz-NWb62VxLeTyqJs8cHaDmFu3GiYoBnQ5tXeKv/view?tab=t.0

```html
<!DOCTYPE html>
<html lang="en">
<head>
<meta charset="utf-8">
<title>Brightvane.xyz — High-Intent Leads</title>
<link href="https://fonts.googleapis.com/css2?family=Montserrat:wght@400;500;600;700;800&display=swap" rel="stylesheet">
<style>
:root{
  --red:#b3191c;
  --red-dark:#6e0f12;
  --ink:#1c1c1c;
  --text:#555;
  --beige:#f5e6c3;
  --card:#f8e8c6;
  --slate:#48484c;
  --gold:#f0a21c;
  --white:#fff;
}
*{box-sizing:border-box;margin:0;padding:0}
html,body{width:1200px;height:5272px;overflow:hidden}
body{font-family:'Montserrat',sans-serif;color:var(--text);background:var(--white);font-size:11px;line-height:1.6}
.wrap{width:888px;margin:0 auto;position:relative}
.btn{display:inline-block;background:var(--red);color:#fff;font-weight:600;font-size:10.5px;padding:8px 18px;border-radius:2px;text-decoration:none}
.center{text-align:center}
h2.title{font-size:27px;font-weight:700;color:var(--red);text-align:center;line-height:1.2}
.sub{text-align:center;font-size:10.5px;color:#333;margin-top:4px}
.block-title{font-weight:700;color:#222;font-size:11.5px}
.block p{font-size:10.5px;color:var(--text)}
.block + .block{margin-top:16px}
.photo{border:6px solid #fff;box-shadow:0 0 10px rgba(0,0,0,.15)}

/* header */
.site-header{height:62px;display:flex;align-items:center;justify-content:space-between;padding:0 156px}
.logo{font-weight:700;font-size:24px;color:var(--ink)}
/* hero */
.hero{height:532px;position:relative;background:linear-gradient(100deg,var(--red-dark) 0%,#8d1216 40%,#231a2a 70%,#16202e 100%);overflow:hidden}
.hero-visual{position:absolute;right:0;top:0;width:620px;height:532px;background:radial-gradient(circle at 65% 55%,#3a4a66 0%,#1d2638 55%,transparent 80%)}
.hero-copy{position:absolute;left:158px;top:124px;width:410px;color:#fff}
.hero-copy h1{font-size:34px;font-weight:800;line-height:1.12;letter-spacing:.3px}
.hero-copy p{font-size:10.5px;margin-top:14px;line-height:1.6}
.hero-copy .lead{color:var(--gold);font-weight:700;margin-top:16px}
.hero-copy .btn{margin-top:20px}
/* results */
.results{height:528px;padding-top:72px}
.results .row{display:flex;align-items:center;margin-top:30px;padding-left:50px}
.results .photo{width:455px;height:236px;background:linear-gradient(135deg,#8c97a5,#5a6270 50%,#c4c8cf)}
.results .copy{margin-left:50px;width:300px}
/* services */
.services{height:468px;background:var(--beige);padding-top:72px}
.svc-grid{display:grid;grid-template-columns:repeat(5,1fr);margin-top:44px;text-align:center}
.svc .icon{width:82px;height:82px;border-radius:50%;background:#fff;border:2px solid #d8823e;margin:0 auto;display:flex;align-items:center;justify-content:center}
.svc h3{font-size:11.5px;color:#222;margin-top:16px;font-weight:700}
.svc p{font-size:10px;width:150px;margin:2px auto 0;line-height:1.6}
/* why */
.why{height:564px;padding-top:72px}
.why .row{display:flex;justify-content:space-between;align-items:center;margin-top:40px}
.why .copy{width:380px}
.why .photo{width:426px;height:262px;background:linear-gradient(120deg,#7a5234,#c9a47a 50%,#3b3a3c)}
/* tailored */
.tailored{height:534px;background:var(--slate);padding-top:72px}
.tailored h2.title{color:var(--gold)}
.tailored .sub{color:#ddd}
.tiles{display:flex;flex-wrap:wrap;justify-content:center;gap:12px;margin-top:24px}
.tile{width:168px;height:121px;background:var(--card);display:flex;flex-direction:column;align-items:center;justify-content:center;text-align:center;color:#333;font-size:11px;font-weight:500;line-height:1.4}
.tile svg{margin-bottom:10px}
/* process */
.process{position:relative;height:952px;background:linear-gradient(var(--slate) 0 132px,var(--beige) 132px)}
.process-card{position:absolute;left:156px;top:0;width:888px;height:530px;background:#fff;padding-top:68px}
.process .row{display:flex;align-items:center;margin-top:30px;padding-left:69px}
.process .photo{width:364px;height:264px;background:linear-gradient(135deg,#dfe6ea,#9fb1bd 55%,#e8ecee);border-width:0;box-shadow:none}
.process .copy{margin-left:42px;width:350px}
.apart{position:absolute;top:560px;left:0;width:1200px}
.apart-grid{display:grid;grid-template-columns:repeat(3,1fr);margin-top:44px;text-align:center}
.num{display:inline-block;width:30px;height:30px;background:var(--slate);color:#fff;font-size:15px;line-height:30px}
.apart-grid h3{font-size:11.5px;color:#222;margin-top:12px;font-weight:700}
.apart-grid p{font-size:10.5px;width:230px;margin:2px auto 0}
/* effortless */
.growth{height:464px;padding-top:76px}
.growth .row{display:flex;justify-content:space-between;align-items:center;margin-top:36px}
.growth .copy{width:380px}
.growth .photo{width:420px;height:221px;background:linear-gradient(160deg,#2e4a6b,#8bb0cf 45%,#5c8a3a 70%,#d4d9dd);border:none;box-shadow:none}
.growth .btn{margin-top:24px}
/* stories */
.stories{height:522px;background:var(--slate);padding-top:72px}
.stories h2.title{color:var(--gold)}
.stories .sub{color:#ddd}
.quotes{display:flex;justify-content:space-between;margin-top:30px;position:relative}
.quote{width:278px;height:217px;background:#fff;padding:42px 18px 0;position:relative}
.quote .mark{position:absolute;left:18px;top:-20px;width:40px;height:40px;border-radius:50%;background:#2a2a2e;border:3px solid #fff;display:flex;align-items:center;justify-content:center;color:#fff;font-size:26px;font-weight:800;line-height:1}
.stars{color:var(--gold);font-size:13px;letter-spacing:1px}
.quote p{font-size:10px;line-height:1.55;margin-top:4px}
.quote .who{color:var(--red);font-weight:700;font-size:10.5px;margin-top:14px}
.quote .role{font-size:9px}
.quote .role b{color:#222}
.arrow{position:absolute;top:100px;color:#aaa;font-size:20px}
/* ready */
.ready{height:461px;padding-top:86px}
.ready h2.title{width:560px;margin:0 auto}
.ready-grid{display:grid;grid-template-columns:repeat(3,1fr);margin-top:40px;text-align:center}
.ready-grid .icon{width:82px;height:82px;border-radius:50%;background:#fdf3dd;border:2px solid #e49a4a;margin:0 auto;display:flex;align-items:center;justify-content:center}
.ready-grid h3{font-size:11.5px;color:#222;margin-top:16px;font-weight:700}
.ready-grid p{font-size:10px;width:200px;margin:0 auto}
/* footer */
.site-footer{height:185px;position:relative;background:linear-gradient(100deg,var(--red-dark),#8d1216 45%,#221a29 75%,#16202e);color:#fff;overflow:hidden}
.site-footer .inner{position:absolute;left:156px;top:44px}
.site-footer .brand{font-size:33px;font-weight:700}
.site-footer .tag{color:var(--gold);font-weight:700;font-size:17px;margin-top:2px}
.site-footer small{font-size:9.5px}
</style>
</head>
<body>

<header class="site-header">
  <div class="logo">brightvane.xyz</div>
  <a class="btn" href="#">Schedule a Free Call Today</a>
</header>

<section class="hero">
  <div class="hero-visual" role="img" aria-label="Businessman's open hand beneath a glowing rising growth arrow"></div>
  <div class="hero-copy">
    <h1>HIGH-INTENT LEADS DELIVERED DIRECTLY TO YOUR PIPELINE</h1>
    <p>Take the guesswork out of lead generation. We connect you with high-intent prospects who are genuinely interested in what you offer, helping you grow your sales pipeline with ease.</p>
    <p class="lead">LET'S TALK ABOUT HOW WE CAN DELIVER THE LEADS YOUR BUSINESS NEEDS.</p>
    <a class="btn" href="#">Schedule a Free Call Today</a>
  </div>
</section>

<section class="results">
  <div class="wrap">
    <h2 class="title">We Deliver Results, Not Promises</h2>
    <p class="sub">At Brightvane.xyz, we specialize in providing conversion-ready leads that fuel sustainable business growth.</p>
    <div class="row">
      <div class="photo" role="img" aria-label="Business professionals with a tablet among office towers"></div>
      <div class="copy">
        <div class="block"><div class="block-title">Entrepreneur-Led Expertise:</div><p>Founded by seasoned entrepreneurs with proven lead generation success.</p></div>
        <div class="block"><div class="block-title">Performance-Based Model:</div><p>No upfront costs—we succeed only when you do.</p></div>
        <div class="block"><div class="block-title">Comprehensive Approach:</div><p>From SEO to PPC campaigns and high-value content creation, we manage it all.</p></div>
      </div>
    </div>
    <div class="center" style="margin-top:40px"><a class="btn" href="#">Schedule a Free Call Today</a></div>
  </div>
</section>

<section class="services">
  <div class="wrap">
    <h2 class="title">Comprehensive End-to-End Lead Generation</h2>
    <p class="sub">We handle everything needed to deliver high-quality leads so you can focus on scaling your business.</p>
    <div class="svc-grid">
      <div class="svc"><div class="icon"><svg width="36" height="36" viewBox="0 0 36 36"><rect x="8" y="4" width="20" height="28" rx="2" fill="none" stroke="#333" stroke-width="2"/><rect x="12" y="9" width="12" height="6" fill="#c9262a"/><path d="M12 20h12M12 25h9" stroke="#333" stroke-width="2"/></svg></div><h3>Content Creation</h3><p>High-value gated content, articles, and blog posts to attract and convert leads.</p></div>
      <div class="svc"><div class="icon"><svg width="36" height="36" viewBox="0 0 36 36"><rect x="4" y="7" width="28" height="22" rx="2" fill="none" stroke="#333" stroke-width="2"/><path d="M4 12h28" stroke="#333" stroke-width="2"/><rect x="12" y="16" width="12" height="9" fill="#c9262a"/></svg></div><h3>Design &amp; Development</h3><p>Professional assets and optimized landing pages for maximum engagement.</p></div>
      <div class="svc"><div class="icon"><svg width="36" height="36" viewBox="0 0 36 36"><path d="M15 30V14a3 3 0 0 1 6 0v8l6 2v6z" fill="none" stroke="#333" stroke-width="2"/><circle cx="18" cy="10" r="7" fill="none" stroke="#c9262a" stroke-width="2"/></svg></div><h3>PPC Campaigns</h3><p>Targeted paid search to drive qualified leads.</p></div>
      <div class="svc"><div class="icon"><svg width="36" height="36" viewBox="0 0 36 36"><circle cx="18" cy="18" r="12" fill="none" stroke="#333" stroke-width="2"/><circle cx="18" cy="18" r="6" fill="#c9262a"/><path d="M18 2v6M18 28v6M2 18h6M28 18h6" stroke="#333" stroke-width="2"/></svg></div><h3>SEO &amp; Social Media</h3><p>Organic strategies to attract quality traffic and generate leads.</p></div>
      <div class="svc"><div class="icon"><svg width="36" height="36" viewBox="0 0 36 36"><circle cx="15" cy="15" r="10" fill="none" stroke="#333" stroke-width="2"/><path d="M22 22l9 9" stroke="#333" stroke-width="3"/><path d="M10 18l4-4 3 3 4-5" fill="none" stroke="#c9262a" stroke-width="2"/></svg></div><h3>Real-Time Optimization</h3><p>Ongoing analysis &amp; adjustments for peak performance and ROI.</p></div>
    </div>
    <div class="center" style="margin-top:36px"><a class="btn" href="#">Schedule a Free Call Today</a></div>
  </div>
</section>

<section class="why">
  <div class="wrap">
    <h2 class="title">Why Choose Brightvane.xyz?</h2>
    <p class="sub">We specialize in delivering high-intent leads that drive measurable growth. Here's how we stand out:</p>
    <div class="row">
      <div class="copy">
        <div class="block"><div class="block-title">Results-Driven Approach:</div><p>We handle all aspects of lead generation, from creating lead magnets to executing advertising and SEO campaigns, delivering high-quality leads that align with your goals.</p></div>
        <div class="block"><div class="block-title">Tailored Strategies:</div><p>Our campaigns are designed to connect you with prospects who are genuinely interested in the type of products or services you offer.</p></div>
        <div class="block"><div class="block-title">Simplified Growth Solutions:</div><p>With all the heavy lifting managed by our team, you can focus entirely on growing your business and closing more deals.</p></div>
      </div>
      <div class="photo" role="img" aria-label="Two colleagues working together at laptops in an office"></div>
    </div>
    <div class="center" style="margin-top:40px"><a class="btn" href="#">Schedule a Free Call Today</a></div>
  </div>
</section>

<section class="tailored">
  <div class="wrap">
    <h2 class="title">Tailored Content for High-Intent Lead Capture</h2>
    <p class="sub">We create custom-crafted content tailored for your audience.</p>
    <div class="tiles">
      <div class="tile"><svg width="36" height="36" viewBox="0 0 36 36"><rect x="9" y="4" width="18" height="28" rx="2" fill="none" stroke="#333" stroke-width="2"/><circle cx="20" cy="12" r="5" fill="#f0a21c"/></svg>Guides and<br>eBooks</div>
      <div class="tile"><svg width="36" height="36" viewBox="0 0 36 36"><rect x="7" y="4" width="20" height="27" fill="none" stroke="#333" stroke-width="2"/><circle cx="25" cy="25" r="6" fill="#c9262a"/><path d="M11 11h12M11 16h8" stroke="#333" stroke-width="2"/></svg>Industry<br>Insights Reports</div>
      <div class="tile"><svg width="36" height="36" viewBox="0 0 36 36"><path d="M6 10h16l-4-4M30 26H14l4 4" fill="none" stroke="#333" stroke-width="2"/><circle cx="26" cy="14" r="4" fill="#f0a21c"/></svg>Infographics &amp;<br>Visual Guides</div>
      <div class="tile"><svg width="36" height="36" viewBox="0 0 36 36"><path d="M4 32h28M8 32V18h6v14M16 32V12h6v20M24 32V8h6v24" fill="none" stroke="#333" stroke-width="2"/><rect x="16" y="12" width="6" height="6" fill="#c9262a"/></svg>Glossary of<br>Industry Terms</div>
      <div class="tile"><svg width="36" height="36" viewBox="0 0 36 36"><rect x="6" y="5" width="24" height="26" fill="none" stroke="#333" stroke-width="2"/><path d="M10 12h16M10 18h16M10 24h10" stroke="#333" stroke-width="2"/></svg>Checklist for<br>Best Practices</div>
      <div class="tile"><svg width="36" height="36" viewBox="0 0 36 36"><path d="M6 32V20M13 32V14M20 32V18M27 32V8" stroke="#333" stroke-width="3"/><path d="M5 16l8-6 7 4 9-9" fill="none" stroke="#c9262a" stroke-width="2"/></svg>Trend Spotting<br>Forecast</div>
      <div class="tile"><svg width="36" height="36" viewBox="0 0 36 36"><rect x="5" y="5" width="26" height="26" fill="none" stroke="#333" stroke-width="2"/><rect x="9" y="9" width="8" height="8" fill="#c9262a"/><path d="M20 11h7M9 22h18M9 26h12" stroke="#333" stroke-width="2"/></svg>Templates<br>and Toolkits</div>
      <div class="tile"><svg width="36" height="36" viewBox="0 0 36 36"><path d="M4 32h28M8 32v-8h6v8M22 32v-12h6v12M15 32V14h6v18" fill="none" stroke="#333" stroke-width="2"/><path d="M18 4v8" stroke="#c9262a" stroke-width="2"/></svg>Competitive<br>Landscape</div>
      <div class="tile"><svg width="36" height="36" viewBox="0 0 36 36"><rect x="12" y="4" width="16" height="20" fill="none" stroke="#333" stroke-width="2"/><rect x="8" y="12" width="16" height="20" fill="#f0a21c"/></svg>Whitepapers</div>
    </div>
    <div class="center" style="margin-top:28px"><a class="btn" href="#">Schedule a Free Call Today</a></div>
  </div>
</section>

<section class="process">
  <div class="process-card">
    <h2 class="title">How We Deliver High-Quality Leads</h2>
    <p class="sub">Our streamlined process ensures you receive ready-to-engage leads without the hassle:</p>
    <div class="row">
      <div class="photo" role="img" aria-label="Hands holding a phone beneath digital gear and data icons"></div>
      <div class="copy">
        <div class="block"><div class="block-title">Precise Market Targeting:</div><p>We start by understanding your ideal customer profile and identifying high-intent prospects in your market.</p></div>
        <div class="block"><div class="block-title">Customized Campaign Execution:</div><p>We take the time to understand your audience, creating and running campaigns tailored to their interests, leveraging insights from advertising, SEO, and lead magnets.</p></div>
        <div class="block"><div class="block-title">All-Inclusive Management:</div><p>From strategy to execution, we handle every detail, delivering leads while you focus on closing deals.</p></div>
      </div>
    </div>
    <div class="center" style="margin-top:30px"><a class="btn" href="#">Schedule a Free Call Today</a></div>
  </div>

  <div class="apart">
    <div class="wrap">
      <h2 class="title">What Sets Us Apart?</h2>
      <p class="sub">We're more than just a lead generation service—our approach ensures valuable opportunities for your business:</p>
      <div class="apart-grid">
        <div><span class="num">01</span><h3>High-Intent Leads</h3><p>The high-intent leads we generate provide a solid starting point for building meaningful connections.</p></div>
        <div><span class="num">02</span><h3>Complete Service</h3><p>We take care of everything needed to generate leads, so you can stay focused on growing your business.</p></div>
        <div><span class="num">03</span><h3>Success-Based Partnership</h3><p>With our results-driven model, you pay only for the leads we deliver, ensuring value every step of the way.</p></div>
      </div>
      <div class="center" style="margin-top:36px"><a class="btn" href="#">Schedule a Free Call Today</a></div>
    </div>
  </div>
</section>

<section class="growth">
  <div class="wrap">
    <h2 class="title">Effortless Growth, Designed for You</h2>
    <p class="sub">We simplify lead generation, so you can focus on growing your business:</p>
    <div class="row">
      <div class="copy">
        <div class="block"><div class="block-title">Hands-Off Convenience:</div><p>We manage the strategy, content, advertising, and optimization, delivering a steady flow of high-quality prospects.</p></div>
        <div class="block"><div class="block-title">Built to Scale:</div><p>Our process adapts to your growth goals, ensuring consistent lead flow whether you're starting small or scaling rapidly.</p></div>
        <a class="btn" href="#">Schedule a Free Call Today</a>
      </div>
      <div class="photo" role="img" aria-label="Businessman tending a plant shaped like a rising growth arrow"></div>
    </div>
  </div>
</section>

<section class="stories">
  <div class="wrap">
    <h2 class="title">Proven Success Stories</h2>
    <p class="sub">Discover how our clients have achieved exceptional growth with Brightvane.xyz:</p>
    <div class="quotes">
      <span class="arrow" style="left:-32px">‹</span>
      <div class="quote"><div class="mark">“</div><div class="stars">★★★★★</div><p>Brightvane.xyz Has Completely Transformed Our Lead Generation Efforts. We've Seen A 35% Increase In High-Quality Leads In Just Three Months.</p><div class="who">Marco T.</div><div class="role">VP Of Sales At A <b>Mid-Sized B2B Firm</b></div></div>
      <div class="quote"><div class="mark">“</div><div class="stars">★★★★★</div><p>The Team At Brightvane.xyz Took Care Of Everything—From Content To Campaigns. Their Performance-Based Model Meant We Only Paid When Results Came In. It's A Win-Win!</p><div class="who">Priya K.</div><div class="role">CEO of a <b>Professional Services Company</b></div></div>
      <div class="quote"><div class="mark">“</div><div class="stars">★★★★★</div><p>Working With Brightvane.xyz Is Like Having An In-House Growth Team. Their Ability To Create And Optimize Content-Driven Campaigns Helped Us Double Our Inbound Inquiries.</p><div class="who">Owen R.</div><div class="role">Marketing Director at a <b>SaaS Company</b></div></div>
      <span class="arrow" style="right:-32px;color:var(--gold)">›</span>
    </div>
    <div class="center" style="margin-top:30px"><a class="btn" href="#">Schedule a Free Call Today</a></div>
  </div>
</section>

<section class="ready">
  <div class="wrap">
    <h2 class="title">Ready to Unlock Scalable Growth for Your Business?</h2>
    <p class="sub">Schedule a call to learn how we can help your business grow predictably and efficiently.</p>
    <div class="ready-grid">
      <div><div class="icon"><svg width="36" height="36" viewBox="0 0 36 36"><circle cx="14" cy="12" r="5" fill="none" stroke="#333" stroke-width="2"/><path d="M5 30c0-6 4-10 9-10s9 4 9 10" fill="none" stroke="#333" stroke-width="2"/><circle cx="26" cy="22" r="5" fill="#f0a21c"/></svg></div><h3>High-Intent Leads</h3><p>that match your ideal customer profile.</p></div>
      <div><div class="icon"><svg width="36" height="36" viewBox="0 0 36 36"><path d="M4 24h8l10 4 10-8-4-2-8 4" fill="none" stroke="#333" stroke-width="2"/><circle cx="20" cy="12" r="6" fill="#f0a21c"/></svg></div><h3>Custom Campaigns</h3><p>designed to engage and convert your audience.</p></div>
      <div><div class="icon"><svg width="36" height="36" viewBox="0 0 36 36"><circle cx="18" cy="18" r="11" fill="none" stroke="#333" stroke-width="2"/><circle cx="18" cy="18" r="5" fill="#f0a21c"/><path d="M18 3v8M18 25v8M3 18h8M25 18h8" stroke="#333" stroke-width="2"/></svg></div><h3>Actionable Insights</h3><p>to optimize performance and scale effectively.</p></div>
    </div>
    <div class="center" style="margin-top:30px"><a class="btn" href="#">Schedule a Free Call Today</a></div>
  </div>
</section>

<footer class="site-footer">
  <div class="hero-visual" role="img" aria-label="Glowing rising growth arrow over a dark backdrop" style="height:185px;background:radial-gradient(circle at 70% 50%,#34425c 0%,transparent 70%)"></div>
  <div class="inner">
    <div class="brand">brightvane xyz</div>
    <div class="tag">Driving Real Growth, One Lead at a Time</div>
    <small>Copyright 2025 Brightvane.xyz, LLC. All rights reserved</small>
  </div>
</footer>

</body>
</html>
```